Christmas Collection Candle Label Design

Looking to update our existing Christmas Candle Collection labels. Labels should reflect the overall feel of our brand- www.kelvabrite.ca
Want to include some color elements. Holiday colors added into design but more muted/ earthy tones not vibrant colors . Metallic elements and line art botanical illustration. Fonts should be more align to brand
Scents
Winter Lantern
Frost Berry
Amber and Fig
Belle Étoile

```html
<!DOCTYPE html>
<html lang="en">
<head>
<meta charset="utf-8">
<title>Kelva Brite – Frost Berry Candle Label</title>
<link rel="stylesheet" href="https://fonts.googleapis.com/css2?family=Libre+Caslon+Text:wght@400;700&family=Lato:wght@400;700&display=swap">
<style>
  :root {
    --backdrop: #ebe5dd;
    --sage: #7a8c6e;
    --cream: #ece6d6;
    --line: #e4ddcc;
    --art-soft: #8b9c7f;
    --art-deep: #a8b59d;
  }
  * { margin: 0; padding: 0; box-sizing: border-box; }
  html, body {
    width: 1200px;
    height: 959px;
    overflow: hidden;
    background: var(--backdrop);
  }
  .canvas {
    position: relative;
    width: 1200px;
    height: 959px;
  }
  .label {
    position: absolute;
    left: 150px;
    top: 180px;
    width: 900px;
    height: 600px;
    background: var(--sage);
    color: var(--cream);
    font-family: "Lato", sans-serif;
  }
  .brand {
    position: absolute;
    top: 52px;
    left: 0;
    width: 100%;
    text-align: center;
  }
  .brand-name {
    font-family: "Libre Caslon Text", serif;
    font-size: 27px;
    letter-spacing: 1px;
    line-height: 1;
  }
  .brand-tagline {
    margin-top: 6px;
    font-size: 9px;
    letter-spacing: 2.4px;
    text-transform: uppercase;
  }
  .rule {
    position: absolute;
    left: 82px;
    width: 731px;
    height: 3px;
    background: var(--line);
  }
  .rule-top { top: 133px; }
  .rule-bottom-a { top: 500px; }
  .rule-bottom-b { top: 555px; }
  .scent-name {
    position: absolute;
    left: 82px;
    top: 182px;
    font-family: "Libre Caslon Text", serif;
    font-weight: 700;
    font-size: 70px;
    line-height: 98px;
    letter-spacing: 2px;
    text-transform: uppercase;
  }
  .scent-note {
    position: absolute;
    left: 82px;
    top: 377px;
    font-size: 18px;
    letter-spacing: 0.4px;
    text-transform: uppercase;
  }
  .botanical-art {
    position: absolute;
    left: 545px;
    top: 165px;
    width: 325px;
    height: 285px;
    border-radius: 6px;
    background: radial-gradient(ellipse at 45% 55%, var(--art-deep), var(--art-soft) 70%, var(--sage));
  }
  .details {
    position: absolute;
    left: 82px;
    top: 515px;
    width: 731px;
    display: flex;
    justify-content: space-between;
    font-size: 21px;
    text-transform: uppercase;
  }
</style>
</head>
<body>
<main class="canvas">
  <section class="label">
    <header class="brand">
      <div class="brand-name">KELVA BRITE</div>
      <div class="brand-tagline">Pure plant based scents</div>
    </header>
    <div class="rule rule-top"></div>
    <h1 class="scent-name">Frost<br>Berry</h1>
    <p class="scent-note">Made with plant based botanical</p>
    <div class="botanical-art" role="img" aria-label="Line-art botanical illustration of lilies in cream outline"></div>
    <div class="rule rule-bottom-a"></div>
    <div class="details">
      <span>13 oz</span>
      <span>//</span>
      <span>Made in Canada</span>
    </div>
    <div class="rule rule-bottom-b"></div>
  </section>
</main>
</body>
</html>
```